Package Design for 15 lines of Tea

I need design variations for 15 different Tea lines.
The tea will be packaged in Tin cylinders.
I have attached several pictures to show you an example of the display we are modelling after along with other references.
The 15 tea lines are:
Study Tea
Ingredients: Brazilian Mate, Mint
Energy Boost Tea
Ingredients: Yunnan Coffee, Dark Puer
Relaxation Tea
Ingredients: Lotus Flower, South African Rooibos
Beauty Tea
Ingredients: Rose, Chrysanthemum, Red Dates, Huangqi
Sore Throat Tea
Ingredients: Honeysuckle, Pang Da Hai, Chamomile, Licorice Root
Get Well Tea
Ingredients: Ginger, Rooibos, Orange peel, Chinese Angelica
Diet Tea
Ingredients: Puer, Hibiscus, Lemongrass, Lotus Plumule
Bedtime Tea
Ingredients: Apple, Orange, Chamomile
South African Rooibos Tea
(pure)
Brazilian Yerba Mate Tea
(pure)
Long Jing Green Tea
(pure)
Darjeeling Black Tea
(pure)
Nepal Golden Tea
(Pure)
Bai Mu Dan White Tea
(pure)
Phoenix Oolong Tea
(pure)
Every Tea Blend should have three unique symbols that describe the purpose and theme of the blend. (!!Please don't make specific reference to the ingredients of the blends because some of these ingredients may be changed later. Stick to focusing on the intended purpose of the tea blend!!)
I would like the symbols to keep the same brushlike style that is consistent with our company logo.
Please keep the three block structure. I suggest keeping to just one color per tea blend. This will help each blend stand out between one another. I have a sample of the "Diet Tea" attached that I did myself to give you an idea of the structure I'm looking for, but obviously it's just my amateur version. Hope you can make them look far more appealing.
The ultimate goal is to build a picture language unique to our brand. As more products are released, we intend to potentially have hundreds of symbols, each with it's own meaning. So it would be nice when you present your pictures if you explain its intended meaning or message.
Deminsions:
Cylinder type 1: 82mm*38mmH
circular labels (along with your design) will be placed on the cap of product, and then the cylinder will be slanted on it's side to display the cap towards the customer.
Cylinder type 2: 65mm*152mmH
the labels will be placed on the side of the cylinder. In this version, try lining the three symbols in a vertical position. If this looks awful to you then feel free to go back to the horizontal style, but it would be nice to see what the vertical version looks like for reference.
Updates
Due to the scope of this project, please take note that I just increased my budget an additional 500 dollars more.
I also just added a 100 dollar second place prize. Don't want to see hard work unrewarded.
Feel free to send a few samples and I will provide prompt feedback. Please don't feel that you must submit all 15 lines at the same time.
Project Deadline Extended
Reason: I am extending the deadline as I feel there are more detailed revisions that need to be made until final selection.
Target Market(s)
Middle to Upper Class Consumers in China
Industry/Entity Type
It Company
Other font styles liked:
- font similar to font on company logo
Requirements
Must have
- Tea Designs must be in harmony with company logo and theme.
Should not have
- Avoid using Chinese characters as symbols. They may seem cool to westerners, but it's tacky for Chinese consumers.

```html
<!DOCTYPE html>
<html lang="en">
<head>
<meta charset="utf-8">
<title>Hollin's Tea – Tin Lid Labels</title>
<link href="https://fonts.googleapis.com/css2?family=Special+Elite&display=swap" rel="stylesheet">
<style>
  :root {
    --ink: #0a0b0c;
    --paper: #ffffff;
    --icon-blue: #7fd0ef;
    --icon-orange: #f5a300;
    --icon-green: #c6dc1c;
    --type: "Special Elite", "Courier New", monospace;
  }
  html, body {
    margin: 0; padding: 0;
    width: 1200px; height: 1000px;
    overflow: hidden;
    background: var(--paper);
  }
  .lid-display { position: relative; width: 1200px; height: 1000px; }

  .tin-lid {
    position: absolute;
    width: 192px; height: 192px;
    box-sizing: border-box;
    border-radius: 50%;
    border: 8px solid var(--rim);
    background: var(--face);
    overflow: hidden;
    font-family: var(--type);
    color: var(--ink);
    text-align: center;
  }
  .tin-lid::after {
    content: "";
    position: absolute;
    inset: 4px;
    border-radius: 50%;
    border: 1px solid rgba(255,255,255,.9);
    pointer-events: none;
  }

  .lid-brand {
    position: absolute; left: 30px; right: 30px; top: 12px;
    font-size: 8px; line-height: 9px; font-weight: 400;
    white-space: nowrap;
  }
  .lid-brand-square {
    display: block; margin: 2px auto 0;
    width: 18px; height: 18px; background: var(--ink);
  }

  .lid-title {
    position: absolute; left: 8px; right: 8px; top: 56px;
    font-size: 16px; line-height: 24px;
    margin: 0; font-weight: 400;
    white-space: nowrap;
  }

  .lid-band {
    position: absolute; left: -10px; right: -10px; top: 110px;
    height: 40px;
    display: flex; justify-content: center; align-items: center; gap: 22px;
  }
  .lid-band svg.band-shape { position: absolute; inset: 0; width: 100%; height: 100%; }
  .band-icon {
    position: relative;
    width: 20px; height: 20px; border-radius: 50%;
  }
  .band-icon--blue { background: var(--icon-blue); }
  .band-icon--orange { background: var(--icon-orange); }
  .band-icon--green { background: var(--icon-green); }

  .lid-ingredients {
    position: absolute; left: 40px; right: 40px; top: 155px;
    font-size: 5px; line-height: 6.5px; letter-spacing: 0;
    text-transform: uppercase; margin: 0;
    white-space: nowrap;
  }

  .lid--sore-throat { --face: #b3cc0f; --rim: #a6c20a; left: 81px;  top: 26px; }
  .lid--get-well    { --face: #b592c0; --rim: #a882b6; left: 301px; top: 26px; }
  .lid--diet        { --face: #f2e400; --rim: #ecdc00; left: 516px; top: 26px; }
  .lid--phoenix     { --face: #d7ccc6; --rim: #cdc1ba; left: 731px; top: 26px; }
  .lid--bai-mu-dan  { --face: #f0f0f0; --rim: #e3e3e3; left: 949px; top: 26px; }
  .lid--relaxation  { --face: #a9d397; --rim: #9ccb88; left: 188px; top: 216px; }
  .lid--beauty      { --face: #e37fb0; --rim: #dc6fa5; left: 403px; top: 216px; }
  .lid--yerba-mate  { --face: #f8c07a; --rim: #f6b466; left: 618px; top: 216px; }
  .lid--nepal       { --face: #e4c777; --rim: #ddbd66; left: 833px; top: 216px; }
  .lid--long-jing   { --face: #a6d8d4; --rim: #98d0cb; left: 296px; top: 407px; }
  .lid--rooibos     { --face: #f29b7a; --rim: #ee8d6a; left: 511px; top: 407px; }
  .lid--energy      { --face: #f39200; --rim: #ef8700; left: 726px; top: 407px; }
  .lid--study       { --face: #84cfee; --rim: #72c6ea; left: 403px; top: 596px; }
  .lid--bedtime     { --face: #b2b8dc; --rim: #a3aad4; left: 618px; top: 596px; }
  .lid--darjeeling  { --face: #a7c3d8; --rim: #98b7cf; left: 511px; top: 786px; }
</style>
</head>
<body>
<svg width="0" height="0" style="position:absolute" aria-hidden="true">
  <defs>
    <symbol id="band" viewBox="0 0 200 40" preserveAspectRatio="none">
      <path d="M0 3 L12 1 L25 3 L40 0 L58 2 L75 1 L92 3 L110 0 L128 2 L146 1 L164 3 L182 1 L200 2 L200 38 L186 40 L170 37 L152 39 L134 38 L116 40 L98 37 L80 39 L62 38 L44 40 L26 37 L10 39 L0 38 Z" fill="#0a0b0c"/>
    </symbol>
  </defs>
</svg>

<main class="lid-display">

  <section class="tin-lid lid--sore-throat">
    <div class="lid-brand">Hollin's Tea<span class="lid-brand-square"></span></div>
    <h2 class="lid-title">Sore Throat<br>Tea</h2>
    <div class="lid-band"><svg class="band-shape"><use href="#band"/></svg>
      <span class="band-icon band-icon--blue" role="img" aria-label="Bandage symbol"></span>
      <span class="band-icon band-icon--orange" role="img" aria-label="Throat symbol"></span>
      <span class="band-icon band-icon--green" role="img" aria-label="Feather symbol"></span>
    </div>
    <p class="lid-ingredients">Honeysuckle, Pang Da Hai,<br>Chamomile, Licorice Root</p>
  </section>

  <section class="tin-lid lid--get-well">
    <div class="lid-brand">Hollin's Tea<span class="lid-brand-square"></span></div>
    <h2 class="lid-title">Get Well<br>Tea</h2>
    <div class="lid-band"><svg class="band-shape"><use href="#band"/></svg>
      <span class="band-icon band-icon--blue" role="img" aria-label="Rising arrow symbol"></span>
      <span class="band-icon band-icon--orange" role="img" aria-label="Health cross symbol"></span>
      <span class="band-icon band-icon--green" role="img" aria-label="Bandage symbol"></span>
    </div>
    <p class="lid-ingredients">Ginger, Rooibos, Orange Peel,<br>Chinese Angelica</p>
  </section>

  <section class="tin-lid lid--diet">
    <div class="lid-brand">Hollin's Tea<span class="lid-brand-square"></span></div>
    <h2 class="lid-title">Diet<br>Tea</h2>
    <div class="lid-band"><svg class="band-shape"><use href="#band"/></svg>
      <span class="band-icon band-icon--blue" role="img" aria-label="Feather symbol"></span>
      <span class="band-icon band-icon--orange" role="img" aria-label="Scale symbol"></span>
      <span class="band-icon band-icon--green" role="img" aria-label="Apple symbol"></span>
    </div>
    <p class="lid-ingredients">Puer, Hibiscus, Lemongrass,<br>Lotus Plumule</p>
  </section>

  <section class="tin-lid lid--phoenix">
    <div class="lid-brand">Hollin's Tea<span class="lid-brand-square"></span></div>
    <h2 class="lid-title">Phoenix<br>Oolong Tea</h2>
    <div class="lid-band"><svg class="band-shape"><use href="#band"/></svg>
      <span class="band-icon band-icon--blue" role="img" aria-label="Steam symbol"></span>
      <span class="band-icon band-icon--orange" role="img" aria-label="Swirl symbol"></span>
      <span class="band-icon band-icon--green" role="img" aria-label="Leaf symbol"></span>
    </div>
  </section>

  <section class="tin-lid lid--bai-mu-dan">
    <div class="lid-brand">Hollin's Tea<span class="lid-brand-square"></span></div>
    <h2 class="lid-title">Bai Mu Dan<br>White Tea</h2>
    <div class="lid-band"><svg class="band-shape"><use href="#band"/></svg>
      <span class="band-icon band-icon--blue" role="img" aria-label="Steam symbol"></span>
      <span class="band-icon band-icon--orange" role="img" aria-label="Swirl symbol"></span>
      <span class="band-icon band-icon--green" role="img" aria-label="Leaf symbol"></span>
    </div>
  </section>

  <section class="tin-lid lid--relaxation">
    <div class="lid-brand">Hollin's Tea<span class="lid-brand-square"></span></div>
    <h2 class="lid-title">Relaxation<br>Tea</h2>
    <div class="lid-band"><svg class="band-shape"><use href="#band"/></svg>
      <span class="band-icon band-icon--blue" role="img" aria-label="Cloud symbol"></span>
      <span class="band-icon band-icon--orange" role="img" aria-label="Meditation symbol"></span>
      <span class="band-icon band-icon--green" role="img" aria-label="Lotus symbol"></span>
    </div>
    <p class="lid-ingredients">Lotus Flower,<br>South African Rooibos</p>
  </section>

  <section class="tin-lid lid--beauty">
    <div class="lid-brand">Hollin's Tea<span class="lid-brand-square"></span></div>
    <h2 class="lid-title">Beauty<br>Tea</h2>
    <div class="lid-band"><svg class="band-shape"><use href="#band"/></svg>
      <span class="band-icon band-icon--blue" role="img" aria-label="Heart symbol"></span>
      <span class="band-icon band-icon--orange" role="img" aria-label="Eye symbol"></span>
      <span class="band-icon band-icon--green" role="img" aria-label="Atom symbol"></span>
    </div>
    <p class="lid-ingredients">Rose, Chrysanthemum,<br>Red Dates, Huangqi</p>
  </section>

  <section class="tin-lid lid--yerba-mate">
    <div class="lid-brand">Hollin's Tea<span class="lid-brand-square"></span></div>
    <h2 class="lid-title">Brazilian<br>Yerba Mate Tea</h2>
    <div class="lid-band"><svg class="band-shape"><use href="#band"/></svg>
      <span class="band-icon band-icon--blue" role="img" aria-label="Steam symbol"></span>
      <span class="band-icon band-icon--orange" role="img" aria-label="Swirl symbol"></span>
      <span class="band-icon band-icon--green" role="img" aria-label="Leaf symbol"></span>
    </div>
  </section>

  <section class="tin-lid lid--nepal">
    <div class="lid-brand">Hollin's Tea<span class="lid-brand-square"></span></div>
    <h2 class="lid-title">Nepal<br>Golden Tea</h2>
    <div class="lid-band"><svg class="band-shape"><use href="#band"/></svg>
      <span class="band-icon band-icon--blue" role="img" aria-label="Steam symbol"></span>
      <span class="band-icon band-icon--orange" role="img" aria-label="Swirl symbol"></span>
      <span class="band-icon band-icon--green" role="img" aria-label="Leaf symbol"></span>
    </div>
  </section>

  <section class="tin-lid lid--long-jing">
    <div class="lid-brand">Hollin's Tea<span class="lid-brand-square"></span></div>
    <h2 class="lid-title">Long Jing<br>Green Tea</h2>
    <div class="lid-band"><svg class="band-shape"><use href="#band"/></svg>
      <span class="band-icon band-icon--blue" role="img" aria-label="Steam symbol"></span>
      <span class="band-icon band-icon--orange" role="img" aria-label="Swirl symbol"></span>
      <span class="band-icon band-icon--green" role="img" aria-label="Leaf symbol"></span>
    </div>
  </section>

  <section class="tin-lid lid--rooibos">
    <div class="lid-brand">Hollin's Tea<span class="lid-brand-square"></span></div>
    <h2 class="lid-title">South African<br>Rooibos Tea</h2>
    <div class="lid-band"><svg class="band-shape"><use href="#band"/></svg>
      <span class="band-icon band-icon--blue" role="img" aria-label="Antelope symbol"></span>
      <span class="band-icon band-icon--orange" role="img" aria-label="Flag symbol"></span>
      <span class="band-icon band-icon--green" role="img" aria-label="Needle leaf symbol"></span>
    </div>
  </section>

  <section class="tin-lid lid--energy">
    <div class="lid-brand">Hollin's Tea<span class="lid-brand-square"></span></div>
    <h2 class="lid-title">Energy Boost<br>Tea</h2>
    <div class="lid-band"><svg class="band-shape"><use href="#band"/></svg>
      <span class="band-icon band-icon--blue" role="img" aria-label="Sun symbol"></span>
      <span class="band-icon band-icon--orange" role="img" aria-label="Lightning symbol"></span>
      <span class="band-icon band-icon--green" role="img" aria-label="Battery symbol"></span>
    </div>
    <p class="lid-ingredients">Yunnan Coffee,<br>Dark Puer</p>
  </section>

  <section class="tin-lid lid--study">
    <div class="lid-brand">Hollin's Tea<span class="lid-brand-square"></span></div>
    <h2 class="lid-title">Study<br>Tea</h2>
    <div class="lid-band"><svg class="band-shape"><use href="#band"/></svg>
      <span class="band-icon band-icon--blue" role="img" aria-label="Light bulb symbol"></span>
      <span class="band-icon band-icon--orange" role="img" aria-label="Open book symbol"></span>
      <span class="band-icon band-icon--green" role="img" aria-label="Magnifier symbol"></span>
    </div>
    <p class="lid-ingredients">Brazilian Mate, Mint</p>
  </section>

  <section class="tin-lid lid--bedtime">
    <div class="lid-brand">Hollin's Tea<span class="lid-brand-square"></span></div>
    <h2 class="lid-title">Bedtime<br>Tea</h2>
    <div class="lid-band"><svg class="band-shape"><use href="#band"/></svg>
      <span class="band-icon band-icon--blue" role="img" aria-label="Pillow symbol"></span>
      <span class="band-icon band-icon--orange" role="img" aria-label="Moon symbol"></span>
      <span class="band-icon band-icon--green" role="img" aria-label="Teddy bear symbol"></span>
    </div>
    <p class="lid-ingredients">Apple, Orange,<br>Chamomile</p>
  </section>

  <section class="tin-lid lid--darjeeling">
    <div class="lid-brand">Hollin's Tea<span class="lid-brand-square"></span></div>
    <h2 class="lid-title">Darjeeling<br>Black Tea</h2>
    <div class="lid-band"><svg class="band-shape"><use href="#band"/></svg>
      <span class="band-icon band-icon--blue" role="img" aria-label="Steam symbol"></span>
      <span class="band-icon band-icon--orange" role="img" aria-label="Swirl symbol"></span>
      <span class="band-icon band-icon--green" role="img" aria-label="Leaf symbol"></span>
    </div>
  </section>

</main>
</body>
</html>
```